Harbor Crest PEO - Web Build for Professional Employment Organization

We need a website built for our new PEO (professional employment organization). This company will offer third party Human Resource services to companies who are looking to outsource:<br/>Recruiting<br/>Administrative Onboarding<br/>New hire training, ongoing training and development<br/>Payroll/compensation processing/services<br/>Employee Relations<br/>Unemployment Claim Facilitation<br/>Benefits Plans and Administration<br/><br/>I have attached the logo below. Please use that as a reference and color match as best as possible. <br/><br/>Here are some of the competitor's websites:<br/>https://www.velmorix.example/ <br/>https://www.quandrel.example/<br/>https://www.quandrel.example/<br/>https://www.tzv.example/<br/>https://www.brindaxo.example/<br/>https://lumbrasto.example/contact-lumbra/<br/><br/>

Target Market(s)

Startups and mid-sized businesses

Number of Pages Required

5+ page

Font styles to use
Sans Serif

Colors
0592cd

Requirements
Must have
• Features Pages
• SEO driven keyword rich content
• Strong focus on our ability to provide unemployment claim facilitation services as well as mandatory training/certification fulfillment
Nice to have
• I'd like to see one mockup with a Live Chat version if possible. In theory, the Live Chat messages would go directly to our front desk person.

```html
<!DOCTYPE html>
<html lang="en">
<head>
<meta charset="utf-8">
<title>Harbor Crest PEO — HR and Payroll Services</title>
<link href="https://fonts.googleapis.com/css2?family=Raleway:ital,wght@0,400;0,500;0,600;0,700;1,400&family=Montserrat:wght@400;500;600;700&display=swap" rel="stylesheet">
<style>
:root{
  --cyan:#1ab4d2;
  --cyan-dark:#0592cd;
  --orange:#f8890d;
  --ink:#1d1d1f;
  --text:#555a60;
  --muted:#8a8f95;
  --line:#dfe3e6;
  --form-bg:#ededee;
  --footer:#0e1216;
  --white:#ffffff;
}
*{box-sizing:border-box;margin:0;padding:0}
html,body{width:1200px;height:5388px;overflow:hidden}
body{font-family:"Montserrat",sans-serif;color:var(--text);background:var(--white);position:relative}
.abs{position:absolute}
h1,h2,h3{font-family:"Raleway",sans-serif;font-weight:600}

/* top bar */
.topbar{position:absolute;top:0;left:0;width:1200px;height:38px;background:#fff;font-size:12px}
.topbar .sales{position:absolute;left:94px;top:11px;color:var(--cyan);display:flex;align-items:center;gap:6px}
.topbar .sales span{color:var(--text)}
.topbar .util{position:absolute;right:88px;top:12px;font-size:9px;font-weight:600;letter-spacing:.3px;color:#333}
.topbar .util a{color:#333;text-decoration:none}
.topbar .util a.active{color:var(--cyan)}
.topbar .util i{font-style:normal;margin:0 8px;color:#999}

/* nav */
.nav{position:absolute;top:38px;left:0;width:1200px;height:70px;background:#f4f4f5;border-top:1px solid var(--line)}
.brand{position:absolute;left:92px;top:14px;font-family:"Montserrat",sans-serif;font-weight:700;color:var(--cyan-dark);text-align:center;line-height:1}
.brand .name{font-size:24px;letter-spacing:.5px}
.brand .sub{font-size:15px;letter-spacing:10px;margin-top:3px}
.nav ul{position:absolute;left:440px;top:28px;list-style:none;display:flex;gap:0;font-size:12px;font-weight:500;color:#444}
.nav li{margin-right:26px}
.nav li.current{color:var(--cyan)}
.nav .demo{position:absolute;right:90px;top:0;width:142px;height:70px;background:var(--cyan);color:#fff;font-size:12px;font-weight:700;display:flex;align-items:center;justify-content:center}

/* hero */
.hero{position:absolute;top:108px;left:0;width:1200px;height:544px}
.hero-photo{position:absolute;inset:0;background:linear-gradient(100deg,#aeb7bf 0%,#d8dde1 35%,#e6e3df 55%,#c9bfb4 75%,#f1f1f0 100%)}
.hero-card{position:absolute;left:100px;top:84px;width:295px;height:368px;background:var(--cyan);padding:60px 30px 0 30px;color:#fff}
.hero-card h1{font-size:31px;line-height:1.05;font-weight:600}
.hero-card p{font-size:12px;margin-top:12px;line-height:1.3}
.hero-card .btn{display:block;width:237px;height:40px;margin-top:14px;font-size:11px;font-weight:600;display:flex;align-items:center;justify-content:center}
.hero-card .btn.light{background:#fff;color:#222;margin-top:16px}
.hero-card .btn.dark{background:#0b0b0b;color:#fff}
.dots{position:absolute;right:28px;top:184px;display:flex;flex-direction:column;gap:7px}
.dots i{width:10px;height:10px;border-radius:50%;background:#222;display:block}
.dots i:first-child{background:var(--cyan)}

/* section heads */
.sec-title{position:absolute;left:0;width:1200px;text-align:center;font-size:29px;color:var(--ink)}
.sec-lead{position:absolute;left:190px;width:820px;text-align:center;font-size:12.5px;line-height:1.65;color:var(--text)}

/* size tiers */
.tier{position:absolute;width:220px;text-align:center;font-size:20px;font-family:"Raleway",sans-serif;font-weight:500}
.tier svg{display:block;margin:0 auto 4px}

/* get started cards */
.gs-card{position:absolute;top:1170px;width:288px;height:193px;background:#fff;box-shadow:0 0 9px rgba(0,0,0,.18);padding:42px 20px 0 112px}
.gs-card svg{position:absolute;left:18px;top:60px}
.gs-card h3{font-size:15px;color:var(--cyan);font-weight:600;letter-spacing:.3px}
.gs-card p{font-size:11px;line-height:1.6;margin-top:6px;color:var(--text)}

/* unemployment band */
.claim{position:absolute;top:1473px;left:0;width:1200px;height:586px;background:var(--cyan);color:#fff}
.claim h2{position:absolute;left:102px;top:88px;font-size:30px;font-weight:500}
.claim .item{position:absolute;left:102px;width:400px;padding-left:38px}
.claim .item svg{position:absolute;left:0;top:2px}
.claim .item h4{font-family:"Montserrat",sans-serif;font-size:13px;font-weight:500}
.claim .item p{font-size:10.5px;line-height:1.9;margin-top:4px;opacity:.95}
.claim .cta{position:absolute;left:138px;top:446px;width:292px;height:42px;background:var(--orange);font-size:12px;font-weight:700;display:flex;align-items:center;justify-content:center}
.claim .photo{position:absolute;top:76px;width:260px;height:416px}

/* service grid */
.svc{position:absolute;width:244px;text-align:center}
.svc svg{display:block;margin:0 auto}
.svc h3{font-family:"Montserrat",sans-serif;font-size:14px;font-weight:500;color:var(--ink);margin-top:8px;line-height:1.3;height:38px;display:flex;align-items:flex-start;justify-content:center}
.svc p{font-size:11px;line-height:1.65;margin-top:8px;padding:0 14px}
.svc .more{display:inline-flex;width:122px;height:30px;margin-top:22px;border:2px solid #d6d9dc;border-radius:16px;font-size:10px;font-weight:700;color:#333;align-items:center;justify-content:center}
.svc.featured{background:#fff;box-shadow:0 0 10px rgba(0,0,0,.2);padding-top:34px;height:296px}
.svc.featured .more{background:var(--cyan);border-color:var(--cyan);color:#fff}

/* industries */
.industry{position:absolute;top:3005px;left:0;width:1200px;height:444px;background:var(--orange);color:#fff}
.industry h2{position:absolute;left:0;width:1200px;top:96px;text-align:center;font-size:29px;font-weight:600}
.ind{position:absolute;font-size:13px;font-weight:600;display:flex;align-items:center;gap:9px}

/* testimonials */
.quote{position:absolute;top:3637px;width:260px;height:290px;border:3px solid var(--cyan);padding:26px 26px 0 32px;background:#fff}
.quote .qm{font-family:"Raleway",sans-serif;font-size:64px;font-weight:700;color:#555;line-height:.6;height:30px}
.quote p{font-size:12px;font-style:italic;line-height:1.8;color:#333;font-family:"Raleway",sans-serif}
.quote .close{font-family:"Raleway",sans-serif;font-size:64px;font-weight:700;color:#555;line-height:.3;display:inline-block;vertical-align:top;margin-left:10px;margin-top:14px}
.quote .stars{color:var(--orange);font-size:15px;letter-spacing:2px;margin-top:12px}
.quote .notch{position:absolute;left:24px;bottom:-17px;width:28px;height:17px;overflow:hidden}
.author{position:absolute;top:3958px;display:flex;align-items:center;gap:14px;font-size:12px;font-style:italic;color:#222;font-family:"Raleway",sans-serif;font-weight:500}
.author .avatar{width:52px;height:52px;border-radius:50%;background:radial-gradient(circle at 50% 40%,#c9a88a,#6d5547)}

/* form */
.lead-form{position:absolute;top:4117px;left:0;width:1200px;height:548px;background:var(--form-bg)}
.lead-form h2{position:absolute;left:0;width:1200px;top:98px;text-align:center;font-size:28px;color:var(--cyan);font-weight:700}
.lead-form .tag{position:absolute;left:0;width:1200px;top:136px;text-align:center;font-size:11px;font-style:italic;color:#333}
.lead-form .phone{position:absolute;left:0;width:1200px;top:152px;text-align:center;font-size:19px;color:var(--orange);font-weight:600;letter-spacing:1px}
.field{position:absolute}
.field label{display:block;font-size:9.5px;color:#555;margin-bottom:4px}
.field .box{height:38px;background:#fff;border:1px solid #cfd3d6}
.field .select{position:relative}
.field .select::after{content:"";position:absolute;right:0;top:0;width:26px;height:36px;border-left:1px solid #cfd3d6}
.field .select svg{position:absolute;right:8px;top:15px}
.submit{position:absolute;left:614px;top:410px;width:370px;height:38px;background:var(--orange);color:#fff;font-family:"Raleway",sans-serif;font-weight:700;font-size:13px;letter-spacing:2px;display:flex;align-items:center;justify-content:center}

/* promo */
.promo{position:absolute;top:4665px;left:0;width:1200px;height:272px;background:var(--cyan);color:#fff}
.promo svg.badge{position:absolute;left:109px;top:54px}
.promo h2{position:absolute;left:240px;top:76px;font-size:29px;font-weight:600}
.promo p{position:absolute;left:240px;top:124px;width:540px;font-size:13px;line-height:1.6}
.promo .b{position:absolute;left:828px;width:278px;height:45px;font-size:13px;font-weight:600;display:flex;align-items:center;justify-content:center}
.promo .b.quote-btn{top:75px;background:var(--orange)}
.promo .b.compare{top:131px;background:#fff;color:#222}

/* footer */
.footer{position:absolute;top:4937px;left:0;width:1200px;height:451px;background:var(--footer);color:#fff}
.fcol{position:absolute;top:68px}
.fcol h4{font-family:"Montserrat",sans-serif;font-weight:400;font-size:13px;letter-spacing:.5px;color:#e6e6e6;padding-bottom:8px;border-bottom:1px solid #555;display:inline-block;margin-bottom:16px}
.fcol ul{list-style:none}
.fcol li{font-size:9.5px;font-weight:500;line-height:22.5px;display:flex;align-items:center;gap:10px;text-transform:uppercase}
.fcol li svg{flex:none}
.fcol.social li{text-transform:none;font-size:10px}
.fcol.social li i{width:13px;height:13px;border-radius:50%;background:var(--orange);display:block}
.copy{position:absolute;top:316px;left:0;width:1200px;text-align:center;font-size:10px}
.copy span{color:var(--orange)}
.foot-brand{position:absolute;top:342px;left:0;width:1200px;text-align:center;color:var(--orange);font-weight:700;line-height:1}
.foot-brand .name{font-size:26px;letter-spacing:.5px}
.foot-brand .sub{font-size:16px;letter-spacing:12px;margin-top:2px}
</style>
</head>
<body>

<header class="topbar">
  <div class="sales">
    <svg width="12" height="12" viewBox="0 0 24 24"><path d="M6.6 10.8a15 15 0 0 0 6.6 6.6l2.2-2.2a1 1 0 0 1 1-.25 11.4 11.4 0 0 0 3.6.57 1 1 0 0 1 1 1V20a1 1 0 0 1-1 1A17 17 0 0 1 3 4a1 1 0 0 1 1-1h3.5a1 1 0 0 1 1 1c0 1.25.2 2.45.57 3.6a1 1 0 0 1-.25 1z" fill="none" stroke="#1ab4d2" stroke-width="2"/></svg>
    Talk to Sales : <span>555-014-2760</span>
  </div>
  <div class="util"><a class="active">LOGIN</a><i>|</i><a>INTEGRATIONS</a><i>|</i><a>PARTNERS</a><i>|</i><a>INVESTORS</a></div>
</header>

<nav class="nav">
  <div class="brand"><div class="name">HARBOR CREST</div><div class="sub">PEO</div></div>
  <ul>
    <li class="current">HOME</li><li>ABOUT</li><li>SOLUTIONS</li><li>RESOURCES</li><li>CAREERS</li><li>CONTACT</li>
  </ul>
  <div class="demo">REQUEST A DEMO</div>
</nav>

<section class="hero">
  <div class="hero-photo" role="img" aria-label="Photo of a smiling businesswoman in an office"></div>
  <div class="hero-card">
    <h1>Simplify HR and payroll</h1>
    <p>Unknown printer took a galley of type and scrambled it</p>
    <div class="btn light">Get a freequote</div>
    <div class="btn dark">Schedule a demo</div>
  </div>
  <div class="dots"><i></i><i></i><i></i></div>
</section>

<h2 class="sec-title" style="top:742px">Solutions built for your organization’s size</h2>
<p class="sec-lead" style="top:790px">Printing and typesetting industry. Lorem Ipsum has been the industry's standard dummy text ever since the 1500s, when an unknown printer took a galley of type and scrambled it to make a type.</p>

<div class="tier" style="left:202px;top:868px;color:#f8890d">
  <svg width="112" height="112" viewBox="0 0 112 112"><circle cx="56" cy="56" r="50" fill="none" stroke="#f8890d" stroke-opacity=".45" stroke-width="9" stroke-dasharray="8 9"/><circle cx="56" cy="56" r="36" fill="#f8890d"/><rect x="44" y="46" width="20" height="20" rx="4" fill="none" stroke="#fff" stroke-width="2.5"/><circle cx="54" cy="42" r="7" fill="none" stroke="#fff" stroke-width="2.5"/><circle cx="66" cy="64" r="6" fill="#f8890d" stroke="#fff" stroke-width="2.5"/></svg>
  1-49 Employees
</div>
<div class="tier" style="left:482px;top:868px;color:#1ab4d2">
  <svg width="112" height="112" viewBox="0 0 112 112"><circle cx="56" cy="56" r="50" fill="none" stroke="#1ab4d2" stroke-opacity=".45" stroke-width="9" stroke-dasharray="8 9"/><circle cx="56" cy="56" r="36" fill="#1ab4d2"/><circle cx="44" cy="50" r="5" fill="none" stroke="#fff" stroke-width="2.2"/><circle cx="56" cy="46" r="5" fill="none" stroke="#fff" stroke-width="2.2"/><circle cx="68" cy="50" r="5" fill="none" stroke="#fff" stroke-width="2.2"/><path d="M36 66a8 8 0 0 1 16 0M48 62a8 8 0 0 1 16 0M60 66a8 8 0 0 1 16 0" fill="none" stroke="#fff" stroke-width="2.2"/></svg>
  50-999 Employees
</div>
<div class="tier" style="left:768px;top:868px;color:#1ab4d2">
  <svg width="112" height="112" viewBox="0 0 112 112"><circle cx="56" cy="56" r="50" fill="none" stroke="#1ab4d2" stroke-opacity=".45" stroke-width="9" stroke-dasharray="8 9"/><circle cx="56" cy="56" r="36" fill="#0b0b0b"/><circle cx="56" cy="48" r="5" fill="#fff"/><circle cx="44" cy="52" r="4" fill="#fff"/><circle cx="68" cy="52" r="4" fill="#fff"/><path d="M46 66a10 9 0 0 1 20 0zM36 66a8 7 0 0 1 12-4v4zM76 66a8 7 0 0 0-12-4v4z" fill="#fff"/></svg>
  1,000+ Employees
</div>

<h2 class="sec-title" style="top:1098px">Get Started Today</h2>

<article class="gs-card" style="left:128px">
  <svg width="84" height="60" viewBox="0 0 84 60"><g fill="none" stroke="#0592cd" stroke-width="5"><circle cx="12" cy="34" r="8"/><circle cx="42" cy="46" r="8"/><circle cx="68" cy="16" r="9"/><path d="M19 38l15 5M48 40l13-17"/></g></svg>
  <h3>CONNECT</h3>
  <p>Printing and typesetting industry. Lorem Ipsum has been the industry's standard dummy text.</p>
</article>
<article class="gs-card" style="left:456px">
  <svg width="84" height="60" viewBox="0 0 84 60"><g fill="none" stroke="#0592cd" stroke-width="3" stroke-linejoin="round"><path d="M4 24l14-12 14 4 10-4 14 4 14 12"/><path d="M18 30l14 14 4-2 4 4 6-2 4 2 10-10"/><path d="M32 26l10-6 16 14"/></g></svg>
  <h3>MEET</h3>
  <p>Printing and typesetting industry. Lorem Ipsum has been the industry's standard dummy text.</p>
</article>
<article class="gs-card" style="left:784px">
  <svg width="84" height="64" viewBox="0 0 84 64"><g fill="#0592cd"><rect x="14" y="44" width="8" height="16"/><rect x="28" y="34" width="8" height="26"/><rect x="42" y="22" width="8" height="38"/></g><path d="M12 34l14-10 10 4 14-12" fill="none" stroke="#0592cd" stroke-width="2.5"/><text x="54" y="14" font-family="Montserrat,sans-serif" font-size="14" font-weight="700" fill="#0592cd">$</text></svg>
  <h3>ELEVATE</h3>
  <p>Printing and typesetting industry. Lorem Ipsum has been the industry's standard dummy text.</p>
</article>

<section class="claim">
  <h2>Unemployment claim</h2>
  <div class="item" style="top:156px">
    <svg width="26" height="22" viewBox="0 0 26 22"><path d="M2 12l7 7L24 3" fill="none" stroke="#fff" stroke-width="4"/></svg>
    <h4>Printing and typesetting industry.</h4>
    <p>Lorem Ipsum has been the industry's standard dummy text ever since the 1500s, when an unknown printer</p>
  </div>
  <div class="item" style="top:250px">
    <svg width="26" height="22" viewBox="0 0 26 22"><path d="M2 12l7 7L24 3" fill="none" stroke="#fff" stroke-width="4"/></svg>
    <h4>Printing and typesetting industry.</h4>
    <p>Lorem Ipsum has been the industry's standard dummy text ever since the 1500s, when an unknown printer</p>
  </div>
  <div class="item" style="top:352px">
    <svg width="26" height="22" viewBox="0 0 26 22"><path d="M2 12l7 7L24 3" fill="none" stroke="#fff" stroke-width="4"/></svg>
    <h4>Printing and typesetting industry.</h4>
    <p>Lorem Ipsum has been the industry's standard dummy text ever since the 1500s, when an unknown printer</p>
  </div>
  <div class="cta">BUILD YOUR COMPLIANCE PLAN</div>
  <div class="photo" role="img" aria-label="Photo of a young man with glasses holding a laptop" style="left:568px;background:linear-gradient(180deg,#d9dcd6,#6c6b4e 60%,#4b4a38)"></div>
  <div class="photo" role="img" aria-label="Photo of a smiling woman with arms crossed" style="left:844px;background:linear-gradient(180deg,#eef0f1,#cfd2d6 55%,#2e2f33)"></div>
</section>

<h2 class="sec-title" style="top:2152px">Payroll and HCM solutions that meet your needs</h2>
<p class="sec-lead" style="top:2200px">Printing and typesetting industry. Lorem Ipsum has been the industry's standard dummy text ever since the 1500s, when an unknown printer took a galley of type and scrambled it to make a type.</p>

<div class="svc featured" style="left:86px;top:2293px">
  <svg width="38" height="38" viewBox="0 0 38 38"><circle cx="16" cy="16" r="11" fill="none" stroke="#1ab4d2" stroke-width="3.5"/><path d="M24 24l10 10" stroke="#1ab4d2" stroke-width="5" stroke-linecap="round"/><circle cx="16" cy="13" r="3.5" fill="#1ab4d2"/><path d="M10 21a6 5 0 0 1 12 0z" fill="#1ab4d2"/></svg>
  <h3>Administrative Onboarding</h3>
  <p>Printing and typesetting industry. Lorem Ipsum has been the industry's standard dummy text.</p>
  <span class="more">READ MORE</span>
</div>
<div class="svc" style="left:357px;top:2327px">
  <svg width="38" height="38" viewBox="0 0 38 38"><circle cx="19" cy="11" r="8" fill="#1ab4d2"/><path d="M8 32a11 10 0 0 1 22 0z" fill="#1ab4d2"/></svg>
  <h3>New hire training</h3>
  <p>Printing and typesetting industry. Lorem Ipsum has been the industry's standard dummy text.</p>
  <span class="more">READ MORE</span>
</div>
<div class="svc" style="left:605px;top:2327px">
  <svg width="38" height="38" viewBox="0 0 38 38"><path d="M12 36V26C5 22 5 10 12 5c7-5 18-2 19 7l3 7h-4v6a3 3 0 0 1-3 3h-4v8z" fill="#1ab4d2"/><circle cx="20" cy="15" r="4" fill="#fff"/></svg>
  <h3>Ongoing training and development</h3>
  <p>Printing and typesetting industry. Lorem Ipsum has been the industry's standard dummy text.</p>
  <span class="more">READ MORE</span>
</div>
<div class="svc" style="left:877px;top:2327px">
  <svg width="38" height="38" viewBox="0 0 38 38"><rect x="10" y="2" width="20" height="28" fill="none" stroke="#1ab4d2" stroke-width="2"/><rect x="6" y="7" width="20" height="29" fill="#fff" stroke="#1ab4d2" stroke-width="2"/><text x="11" y="27" font-family="Montserrat,sans-serif" font-size="14" font-weight="600" fill="#1ab4d2">$</text></svg>
  <h3>Payroll</h3>
  <p>Printing and typesetting industry. Lorem Ipsum has been the industry's standard dummy text.</p>
  <span class="more">READ MORE</span>
</div>

<div class="svc" style="left:80px;top:2654px">
  <svg width="38" height="38" viewBox="0 0 38 38"><circle cx="19" cy="19" r="12" fill="none" stroke="#1ab4d2" stroke-width="6" stroke-dasharray="5 4"/><circle cx="19" cy="19" r="9" fill="#1ab4d2"/><text x="15" y="24" font-family="Montserrat,sans-serif" font-size="12" font-weight="700" fill="#fff">$</text></svg>
  <h3>Compensation processing Services</h3>
  <p>Printing and typesetting industry. Lorem Ipsum has been the industry's standard dummy text.</p>
  <span class="more">READ MORE</span>
</div>
<div class="svc" style="left:357px;top:2654px">
  <svg width="38" height="38" viewBox="0 0 38 38"><circle cx="19" cy="9" r="6" fill="none" stroke="#1ab4d2" stroke-width="4" stroke-dasharray="3 2.5"/><path d="M8 34a11 12 0 0 1 22 0z" fill="#1ab4d2"/></svg>
  <h3>Compensation processing Services</h3>
  <p>Printing and typesetting industry. Lorem Ipsum has been the industry's standard dummy text.</p>
  <span class="more">READ MORE</span>
</div>
<div class="svc" style="left:605px;top:2654px">
  <svg width="40" height="38" viewBox="0 0 40 38"><path d="M18 32V4h2v28" fill="#1ab4d2"/><path d="M20 4l12 5-12 5z" fill="#1ab4d2"/><ellipse cx="19" cy="33" rx="16" ry="4" fill="#1ab4d2"/></svg>
  <h3>Claim Facilitation</h3>
  <p>Printing and typesetting industry. Lorem Ipsum has been the industry's standard dummy text.</p>
  <span class="more">READ MORE</span>
</div>
<div class="svc" style="left:877px;top:2654px">
  <svg width="40" height="38" viewBox="0 0 40 38"><path d="M3 10h12l3 4h19v20H3z" fill="#1ab4d2"/><rect x="20" y="20" width="14" height="12" fill="#fff"/><path d="M22 23h10M22 26h10M22 29h10" stroke="#1ab4d2" stroke-width="1.2"/></svg>
  <h3>Benefits Plans and Administration</h3>
  <p>Printing and typesetting industry. Lorem Ipsum has been the industry's standard dummy text.</p>
  <span class="more">READ MORE</span>
</div>

<section class="industry">
  <h2>Industry experience to address your challenges</h2>
  <div class="ind" style="left:184px;top:186px"><svg width="18" height="16" viewBox="0 0 18 16"><path d="M2 12h14M4 12a5 5 0 0 1 10 0M9 5V3" fill="none" stroke="#fff" stroke-width="1.8"/></svg>Hospitality/Restaurant</div>
  <div class="ind" style="left:470px;top:186px"><svg width="18" height="16" viewBox="0 0 18 16"><circle cx="9" cy="5" r="4" fill="#fff"/><path d="M2 16a7 6 0 0 1 14 0z" fill="#fff"/></svg>Manufacturing</div>
  <div class="ind" style="left:775px;top:186px"><svg width="18" height="16" viewBox="0 0 18 16"><circle cx="9" cy="5" r="4" fill="#fff"/><path d="M2 16a7 6 0 0 1 14 0z" fill="#fff"/></svg>Professional &amp; Technical</div>
  <div class="ind" style="left:184px;top:240px"><svg width="18" height="16" viewBox="0 0 18 16"><path d="M1 15h16M3 15V7h5v8M10 15V3h5v12" fill="none" stroke="#fff" stroke-width="1.8"/></svg>Construction</div>
  <div class="ind" style="left:470px;top:240px"><svg width="18" height="16" viewBox="0 0 18 16"><rect x="1" y="4" width="16" height="10" rx="1" fill="none" stroke="#fff" stroke-width="1.8"/><circle cx="9" cy="9" r="2.5" fill="#fff"/></svg>Financial Services</div>
  <div class="ind" style="left:775px;top:240px"><svg width="18" height="16" viewBox="0 0 18 16"><path d="M1 2h3l2 9h9l2-6H5" fill="none" stroke="#fff" stroke-width="1.8"/><circle cx="7" cy="14" r="1.5" fill="#fff"/><circle cx="14" cy="14" r="1.5" fill="#fff"/></svg>Retail</div>
  <div class="ind" style="left:184px;top:295px"><svg width="18" height="16" viewBox="0 0 18 16"><path d="M7 1h4v5h5v4h-5v5H7v-5H2V6h5z" fill="#fff"/></svg>Health Care</div>
  <div class="ind" style="left:470px;top:295px"><svg width="18" height="16" viewBox="0 0 18 16"><path d="M1 5l8-4 8 4zM2 15h14M4 6v8M7 6v8M11 6v8M14 6v8" fill="#fff" stroke="#fff" stroke-width="1.5"/></svg>Government/Education</div>
  <div class="ind" style="left:775px;top:295px"><svg width="18" height="16" viewBox="0 0 18 16"><path d="M9 15S1 10 1 5a4 4 0 0 1 8-1 4 4 0 0 1 8 1c0 5-8 10-8 10z" fill="#fff"/></svg>Nonprofit/Social Services</div>
</section>

<h2 class="sec-title" style="top:3532px">Testimonials</h2>

<blockquote class="quote" style="left:171px">
  <div class="qm">“</div>
  <p>Printing and typesetting industry. Lorem Ipsum has been the industry's standard dummy text ever since the 1500s, when an unknown printer took a galley of type and scrambled it to make a type s<span class="close">”</span></p>
  <div class="stars">★★★★★</div>
  <svg class="notch" viewBox="0 0 28 17"><path d="M0 0l14 15L28 0" fill="#fff" stroke="#1ab4d2" stroke-width="3"/></svg>
</blockquote>
<blockquote class="quote" style="left:477px">
  <div class="qm">“</div>
  <p>Printing and typesetting industry. Lorem Ipsum has been the industry's standard dummy text ever since the 1500s, when an unknown printer took a galley of type and scrambled it to make a type s<span class="close">”</span></p>
  <div class="stars">★★★★★</div>
  <svg class="notch" viewBox="0 0 28 17"><path d="M0 0l14 15L28 0" fill="#fff" stroke="#1ab4d2" stroke-width="3"/></svg>
</blockquote>
<blockquote class="quote" style="left:782px">
  <div class="qm">“</div>
  <p>Printing and typesetting industry. Lorem Ipsum has been the industry's standard dummy text ever since the 1500s, when an unknown printer took a galley of type and scrambled it to make a type s<span class="close">”</span></p>
  <div class="stars">★★★★★</div>
  <svg class="notch" viewBox="0 0 28 17"><path d="M0 0l14 15L28 0" fill="#fff" stroke="#1ab4d2" stroke-width="3"/></svg>
</blockquote>

<div class="author" style="left:190px"><div class="avatar" role="img" aria-label="Portrait of the reviewer"></div>Dana Whitlow</div>
<div class="author" style="left:492px"><div class="avatar" role="img" aria-label="Portrait of the reviewer"></div>Dana Whitlow</div>
<div class="author" style="left:800px"><div class="avatar" role="img" aria-label="Portrait of the reviewer"></div>Dana Whitlow</div>

<section class="lead-form">
  <h2>Get Started</h2>
  <div class="tag">Let's find the perfect solution for your business.</div>
  <div class="phone">555-019-4831</div>
  <div class="field" style="left:221px;top:216px;width:370px"><label>First Name :</label><div class="box"></div></div>
  <div class="field" style="left:614px;top:216px;width:370px"><label>Last Name :</label><div class="box"></div></div>
  <div class="field" style="left:221px;top:276px;width:370px"><label>Email :</label><div class="box"></div></div>
  <div class="field" style="left:614px;top:276px;width:370px"><label>Phone Number :</label><div class="box"></div></div>
  <div class="field" style="left:221px;top:337px;width:370px"><label>Business Name :</label><div class="box"></div></div>
  <div class="field" style="left:614px;top:337px;width:180px"><label># of Employees :</label><div class="box"></div></div>
  <div class="field" style="left:804px;top:337px;width:180px"><label>ZIP Code :</label><div class="box"></div></div>
  <div class="field" style="left:221px;top:397px;width:370px"><label>Country :</label><div class="box select"><svg width="10" height="6" viewBox="0 0 10 6"><path d="M0 0h10L5 6z" fill="#666"/></svg></div></div>
  <div class="submit">SUBMIT NOW</div>
</section>

<section class="promo">
  <svg class="badge" width="108" height="122" viewBox="0 0 108 122"><circle cx="54" cy="61" r="48" fill="none" stroke="#fff" stroke-width="7" stroke-dasharray="10 5"/><circle cx="54" cy="61" r="36" fill="none" stroke="#fff" stroke-width="5"/><path d="M38 79L70 43" stroke="#fff" stroke-width="6" stroke-linecap="round"/><circle cx="40" cy="48" r="7" fill="none" stroke="#fff" stroke-width="5"/><circle cx="68" cy="74" r="7" fill="none" stroke="#fff" stroke-width="5"/></svg>
  <h2>Get 3 months FREE!</h2>
  <p>Printing and typesetting industry. Lorem Ipsum has been the industry's standard dummy text ever since the 1500s, when an unknown printer took a galley of type and scrambled it to make a type s</p>
  <div class="b quote-btn">START QUOTE</div>
  <div class="b compare">COMPARE PACKAGES</div>
</section>

<footer class="footer">
  <div class="fcol" style="left:104px"><h4>Sitemap</h4><ul>
    <li><svg width="10" height="8" viewBox="0 0 10 8"><path d="M0 4h8M5 1l3 3-3 3" fill="none" stroke="#f8890d" stroke-width="1.6"/></svg>HOME</li>
    <li><svg width="10" height="8" viewBox="0 0 10 8"><path d="M0 4h8M5 1l3 3-3 3" fill="none" stroke="#f8890d" stroke-width="1.6"/></svg>ABOUT</li>
    <li><svg width="10" height="8" viewBox="0 0 10 8"><path d="M0 4h8M5 1l3 3-3 3" fill="none" stroke="#f8890d" stroke-width="1.6"/></svg>SOLUTIONS</li>
    <li><svg width="10" height="8" viewBox="0 0 10 8"><path d="M0 4h8M5 1l3 3-3 3" fill="none" stroke="#f8890d" stroke-width="1.6"/></svg>RESOURCES</li>
    <li><svg width="10" height="8" viewBox="0 0 10 8"><path d="M0 4h8M5 1l3 3-3 3" fill="none" stroke="#f8890d" stroke-width="1.6"/></svg>CAREERS</li>
    <li><svg width="10" height="8" viewBox="0 0 10 8"><path d="M0 4h8M5 1l3 3-3 3" fill="none" stroke="#f8890d" stroke-width="1.6"/></svg>CONTACT</li>
  </ul></div>
  <div class="fcol" style="left:265px"><h4>Who We Serve</h4><ul>
    <li><svg width="10" height="8" viewBox="0 0 10 8"><path d="M0 4h8M5 1l3 3-3 3" fill="none" stroke="#f8890d" stroke-width="1.6"/></svg>Unknown</li>
    <li><svg width="10" height="8" viewBox="0 0 10 8"><path d="M0 4h8M5 1l3 3-3 3" fill="none" stroke="#f8890d" stroke-width="1.6"/></svg>Printer took a</li>
    <li><svg width="10" height="8" viewBox="0 0 10 8"><path d="M0 4h8M5 1l3 3-3 3" fill="none" stroke="#f8890d" stroke-width="1.6"/></svg>Galley of type</li>
    <li><svg width="10" height="8" viewBox="0 0 10 8"><path d="M0 4h8M5 1l3 3-3 3" fill="none" stroke="#f8890d" stroke-width="1.6"/></svg>And scrambled it</li>
    <li><svg width="10" height="8" viewBox="0 0 10 8"><path d="M0 4h8M5 1l3 3-3 3" fill="none" stroke="#f8890d" stroke-width="1.6"/></svg>To make a type</li>
    <li><svg width="10" height="8" viewBox="0 0 10 8"><path d="M0 4h8M5 1l3 3-3 3" fill="none" stroke="#f8890d" stroke-width="1.6"/></svg>Specimen book</li>
  </ul></div>
  <div class="fcol" style="left:455px"><h4>Resources</h4><ul>
    <li><svg width="10" height="8" viewBox="0 0 10 8"><path d="M0 4h8M5 1l3 3-3 3" fill="none" stroke="#f8890d" stroke-width="1.6"/></svg>Unknown printer</li>
    <li><svg width="10" height="8" viewBox="0 0 10 8"><path d="M0 4h8M5 1l3 3-3 3" fill="none" stroke="#f8890d" stroke-width="1.6"/></svg>Took a galley of</li>
    <li><svg width="10" height="8" viewBox="0 0 10 8"><path d="M0 4h8M5 1l3 3-3 3" fill="none" stroke="#f8890d" stroke-width="1.6"/></svg>Type and</li>
    <li><svg width="10" height="8" viewBox="0 0 10 8"><path d="M0 4h8M5 1l3 3-3 3" fill="none" stroke="#f8890d" stroke-width="1.6"/></svg>Scrambled it to</li>
    <li><svg width="10" height="8" viewBox="0 0 10 8"><path d="M0 4h8M5 1l3 3-3 3" fill="none" stroke="#f8890d" stroke-width="1.6"/></svg>Make a type</li>
    <li><svg width="10" height="8" viewBox="0 0 10 8"><path d="M0 4h8M5 1l3 3-3 3" fill="none" stroke="#f8890d" stroke-width="1.6"/></svg>Specimen book</li>
  </ul></div>
  <div class="fcol" style="left:629px"><h4>What We Offer</h4><ul>
    <li><svg width="10" height="8" viewBox="0 0 10 8"><path d="M0 4h8M5 1l3 3-3 3" fill="none" stroke="#f8890d" stroke-width="1.6"/></svg>Unknown printer</li>
    <li><svg width="10" height="8" viewBox="0 0 10 8"><path d="M0 4h8M5 1l3 3-3 3" fill="none" stroke="#f8890d" stroke-width="1.6"/></svg>Took a galley of</li>
    <li><svg width="10" height="8" viewBox="0 0 10 8"><path d="M0 4h8M5 1l3 3-3 3" fill="none" stroke="#f8890d" stroke-width="1.6"/></svg>Type and</li>
    <li><svg width="10" height="8" viewBox="0 0 10 8"><path d="M0 4h8M5 1l3 3-3 3" fill="none" stroke="#f8890d" stroke-width="1.6"/></svg>Scrambled it to</li>
    <li><svg width="10" height="8" viewBox="0 0 10 8"><path d="M0 4h8M5 1l3 3-3 3" fill="none" stroke="#f8890d" stroke-width="1.6"/></svg>Make a type</li>
    <li><svg width="10" height="8" viewBox="0 0 10 8"><path d="M0 4h8M5 1l3 3-3 3" fill="none" stroke="#f8890d" stroke-width="1.6"/></svg>Specimen book</li>
  </ul></div>
  <div class="fcol" style="left:823px"><h4>Integration</h4><ul>
    <li><svg width="10" height="8" viewBox="0 0 10 8"><path d="M0 4h8M5 1l3 3-3 3" fill="none" stroke="#f8890d" stroke-width="1.6"/></svg>Unknown</li>
    <li><svg width="10" height="8" viewBox="0 0 10 8"><path d="M0 4h8M5 1l3 3-3 3" fill="none" stroke="#f8890d" stroke-width="1.6"/></svg>Printer took a</li>
    <li><svg width="10" height="8" viewBox="0 0 10 8"><path d="M0 4h8M5 1l3 3-3 3" fill="none" stroke="#f8890d" stroke-width="1.6"/></svg>Galley of type</li>
    <li><svg width="10" height="8" viewBox="0 0 10 8"><path d="M0 4h8M5 1l3 3-3 3" fill="none" stroke="#f8890d" stroke-width="1.6"/></svg>And scrambled it</li>
    <li><svg width="10" height="8" viewBox="0 0 10 8"><path d="M0 4h8M5 1l3 3-3 3" fill="none" stroke="#f8890d" stroke-width="1.6"/></svg>To make a type</li>
    <li><svg width="10" height="8" viewBox="0 0 10 8"><path d="M0 4h8M5 1l3 3-3 3" fill="none" stroke="#f8890d" stroke-width="1.6"/></svg>Specimen book</li>
  </ul></div>
  <div class="fcol social" style="left:984px"><h4>Connect</h4><ul>
    <li><i></i>Friendnest</li>
    <li><i></i>Chirply</li>
    <li><i></i>Workloop</li>
    <li><i></i>Streamtube</li>
  </ul></div>
  <div class="copy">Copyright © 2020 <span>Harbor Crest</span></div>
  <div class="foot-brand"><div class="name">HARBOR CREST</div><div class="sub">PEO</div></div>
</footer>

</body>
</html>
```